Honey Label Design (145 × 55 mm) – Premium / Minimal Style

Project Description
I am looking for a professional label design for a 500 g honey jar (twist-off, copper-colored lid).
The design should look premium, elegant, and minimal, reflecting natural quality and regional authenticity.
I expect two design proposals from each designer:

One concept based strictly on my color and style guidelines
One completely free creative concept (designer's own interpretation)

⚠️ Important: The layout and positioning of all elements must follow my specifications exactly (see below). Creativity is welcome in style, colors, and typography—but not in layout structure and content.

Label Size and Constraints

Final size: 145 mm × 55 mm (landscape)
All elements must remain fully within the label area
No part (especially the hexagon) may extend beyond the label boundaries

Design Style

Minimal, clean, premium
No clutter, no excessive colors
Preferred colors:

Warm natural tones (honey, beige, brown)
Inspired by the branding of: www.wabenhof-laden. de
Subtle copper tone accents (to match the lid)

Background

Very subtle illustrated/sketched background
Motif:

Wildflower meadow (foreground)
Mixed forest (background)

Style should be fine line / sketch style, not photorealistic
The background must remain very soft so text remains clearly readable

Central Element (Mandatory)

A hexagon (honeycomb shape) centered on the label
Inside text:

“GERMAN HONEY”
“500 g”

The hexagon must be:

Fully inside the label (no overlapping, my example is wrong)
Visually balanced and centered

Left Text Block (Important)
The following content (in german) must be placed left-aligned (not centered!):
Bottling point:
Henrik Dollmann Beekeeping
Lindenkamper Weg 17
99817 Wabenfeld
Tel.: 03671 5274061
mail@wabenhof-laden.example
Typography must be clean and clearly structured.

Mandatory White Fields (Very Important)
There must be exactly 3 white boxes:
Size:

Each: 28 mm × 12 mm
No visible border

Positioning (must follow exactly):

Bottom center

Completely blank (for honey type)

Right side – upper field

Text above: “Best before:”

Right side – lower field (directly below)

Text above: “Lot number”

⚠️ All three fields must:

Be identical in size
Be perfectly aligned
Match the layout shown in the reference image

Layout Rules (Strict)

The arrangement of elements is fixed and must not be changed
Center field must be directly below the hexagon
Right-side fields must be vertically aligned
Left text must remain left-aligned

goal
The label should communicate:

High quality / premium honey
Regional trust and authenticity
Clean and professional print-ready design

Reference
A reference image is provided showing:

exact placement of all fields
general layout structure

⚠️ The reference is for layout guidance only — not for copying design style.
Updates

All mandatory information must be in German like the address
Bottling point:
Henrik Dollmann Beekeeping
Lindenkamper W. 17
99817 Wabenfeld
Tel.: 03671 5274061
www.wabenhof-laden.example

Target Market(s)

Germany

Font styles to use
Sans Serif
Other font styles liked:
• Montserrat, Open Sans, Libre Baskerville

Colors
00AB8E
00BBA5
67D7C9
C6EFE9
E9F9F6
59FF00
82FF00
B8FF75
E3FFCB
F4FFEA
FFF300
FFF600
FEFA6F
FFFEC7
FFFEE8
FFC000
F8CF3A
FAE287
FDF2CF
FEFAEE
F0912C
F2A743
F7CA91
FBE8D2
FDF5EE
EE7325
F08F49
F5BC92
FAE3D3
FDF4ED

Requirements
Must have
• Mandatory Information on Honey Labels (Germany / EU) (Product Name, Country of origin, Net quantity, Minimum durability date (placeholder), Name and address of the food business operator, Batch / lot identification (placeholder), Special warning for infants “Not suitable for infants under 12 months”

```html
<!DOCTYPE html>
<html lang="de">
<head>
<meta charset="utf-8">
<title>Deutscher Honig 500 g – Etikett</title>
<link rel="stylesheet" href="https://fonts.googleapis.com/css2?family=Libre+Baskerville:wght@400;700&family=Open+Sans:wght@400;600;700&display=swap">
<style>
  :root {
    --paper: #f6e6c6;
    --paper-light: #faefd8;
    --paper-edge: #efd8ae;
    --copper: #b86a3a;
    --copper-dark: #7a3b1c;
    --copper-light: #e0a070;
    --ink: #4a2a17;
    --ink-soft: #5a3a26;
    --field: #fffdf8;
  }
  * { margin: 0; padding: 0; box-sizing: border-box; }
  html, body { width: 1200px; height: 456px; overflow: hidden; background: var(--paper); }

  .label {
    position: relative;
    width: 1200px;
    height: 456px;
    background: radial-gradient(ellipse at 50% 45%, var(--paper-light) 0%, var(--paper) 65%, var(--paper-edge) 100%);
    font-family: "Open Sans", sans-serif;
    color: var(--ink);
    overflow: hidden;
  }
  .label__frame {
    position: absolute;
    inset: 9px;
    border: 2px solid var(--copper);
    border-radius: 10px;
  }
  .label__frame::after {
    content: "";
    position: absolute;
    inset: 4px;
    border: 1px solid var(--copper-light);
    border-radius: 7px;
  }

  .scenery-forest {
    position: absolute;
    left: 100px; right: 100px; top: 55px; height: 170px;
    background: linear-gradient(180deg, rgba(217,185,136,0) 0%, rgba(217,185,136,0.35) 55%, rgba(217,185,136,0.12) 100%);
    border-radius: 40% 40% 10% 10%;
  }
  .scenery-flowers {
    position: absolute;
    top: 80px; bottom: 20px; width: 90px;
    background: linear-gradient(180deg, rgba(217,185,136,0.08), rgba(217,185,136,0.38));
  }
  .scenery-flowers--left { left: 16px; border-radius: 40px 40px 0 0; }
  .scenery-flowers--right { right: 16px; width: 130px; top: 95px; border-radius: 60px 60px 0 0; }

  .brand {
    position: absolute;
    left: 110px; top: 62px;
    display: flex; align-items: center; gap: 12px;
  }
  .brand__dot {
    width: 44px; height: 44px; border-radius: 50%;
    background: var(--copper);
  }
  .brand__name {
    font-size: 27px; font-weight: 600; color: var(--ink-soft); letter-spacing: 0.5px;
  }

  .bottler {
    position: absolute;
    left: 129px; top: 212px;
    color: var(--ink-soft);
  }
  .bottler__label { font-size: 15px; line-height: 24px; }
  .bottler__name { font-size: 20px; font-weight: 700; line-height: 30px; color: var(--ink); margin-top: 2px; }
  .bottler__line { font-size: 18px; line-height: 26px; }
  .bottler__phone { font-size: 18px; font-weight: 700; line-height: 28px; color: var(--ink); margin-top: 1px; }
  .bottler__mail { font-size: 14px; line-height: 22px; }

  .warning {
    position: absolute;
    left: 129px; top: 394px;
    display: flex; align-items: center; gap: 7px;
    font-size: 12.5px; color: var(--ink);
  }

  .hexagon {
    position: absolute;
    left: 442px; top: 20px;
    width: 316px; height: 344px;
  }
  .hexagon svg { position: absolute; inset: 0; }
  .hexagon__text {
    position: absolute; inset: 0;
    display: flex; flex-direction: column; align-items: center;
    font-family: "Libre Baskerville", serif;
    color: var(--copper-dark);
  }
  .hexagon__origin { margin-top: 104px; font-size: 33px; font-weight: 700; letter-spacing: 0.5px; line-height: 42px; }
  .hexagon__product { margin-top: 4px; font-size: 62px; font-weight: 700; letter-spacing: 1px; line-height: 1; }
  .hexagon__weight { margin-top: 14px; font-size: 33px; font-weight: 700; color: var(--ink); line-height: 41px; }

  .blank-field {
    position: absolute;
    background: var(--field);
    border-radius: 2px;
  }
  .blank-field--variety { left: 453px; top: 371px; width: 295px; height: 53px; }
  .blank-field--best-before { left: 822px; top: 233px; width: 226px; height: 56px; }
  .blank-field--lot { left: 822px; top: 329px; width: 226px; height: 58px; }

  .field-caption {
    position: absolute;
    left: 822px; width: 226px;
    text-align: center;
    font-size: 16px; line-height: 22px; color: var(--ink);
  }
  .field-caption--best-before { top: 206px; }
  .field-caption--lot { top: 302px; }
</style>
</head>
<body>
<main class="label">
  <div class="scenery-forest" role="img" aria-label="Zart skizzierter Mischwald im Hintergrund"></div>
  <div class="scenery-flowers scenery-flowers--left" role="img" aria-label="Feine Wildblumen-Skizze am linken Rand"></div>
  <div class="scenery-flowers scenery-flowers--right" role="img" aria-label="Feine Wildblumen-Skizze am rechten Rand"></div>
  <div class="label__frame"></div>

  <div class="brand">
    <span class="brand__dot"></span>
    <span class="brand__name">Wabenhof Laden</span>
  </div>

  <section class="bottler">
    <p class="bottler__label">Abfüllstelle:</p>
    <p class="bottler__name">Imkerei Henrik Dollmann</p>
    <p class="bottler__line">Lindenkamper W. 17</p>
    <p class="bottler__line">99817 Wabenfeld</p>
    <p class="bottler__phone">Tel: 09951 5274061</p>
    <p class="bottler__mail">mail@wabenhof-laden.example</p>
  </section>

  <p class="warning">
    <svg width="26" height="26" viewBox="0 0 26 26" aria-hidden="true">
      <circle cx="13" cy="13" r="11" fill="none" stroke="#4a2a17" stroke-width="2"/>
      <line x1="5.5" y1="5.5" x2="20.5" y2="20.5" stroke="#4a2a17" stroke-width="2"/>
    </svg>
    Nicht geeignet für Säuglinge unter 12 Monaten
  </p>

  <div class="hexagon">
    <svg viewBox="0 0 316 344" aria-hidden="true">
      <defs>
        <linearGradient id="copperStroke" x1="0" y1="0" x2="1" y2="1">
          <stop offset="0" stop-color="#e6a57a"/>
          <stop offset="0.5" stop-color="#a8552a"/>
          <stop offset="1" stop-color="#d48a5a"/>
        </linearGradient>
        <radialGradient id="hexFill" cx="0.5" cy="0.4" r="0.6">
          <stop offset="0" stop-color="#fbf1de"/>
          <stop offset="1" stop-color="#f1dfbd"/>
        </radialGradient>
      </defs>
      <polygon points="158,3 313,88 313,256 158,341 3,256 3,88" fill="url(#copperStroke)"/>
      <polygon points="158,13 304,93 304,251 158,331 12,251 12,93" fill="#f3e0c2"/>
      <polygon points="158,19 298,96 298,248 158,325 18,248 18,96" fill="url(#copperStroke)"/>
      <polygon points="158,28 290,101 290,243 158,316 26,243 26,101" fill="url(#hexFill)"/>
      <polygon points="158,34 284,104 284,240 158,310 32,240 32,104" fill="none" stroke="#b86a3a" stroke-width="1.5"/>
    </svg>
    <div class="hexagon__text">
      <span class="hexagon__origin">DEUTSCHER</span>
      <span class="hexagon__product">HONIG</span>
      <span class="hexagon__weight">500 g</span>
    </div>
  </div>

  <div class="blank-field blank-field--variety"></div>

  <p class="field-caption field-caption--best-before">Mindestens haltbar bis</p>
  <div class="blank-field blank-field--best-before"></div>
  <p class="field-caption field-caption--lot">Losnummer</p>
  <div class="blank-field blank-field--lot"></div>
</main>
</body>
</html>
```